Comic book online retailer needs web design

Need a website designed for us to upload via FTP.
Our business is selling comic books and super hero related collectibles through Tradoo exclusively. Our logo has been uploaded. Our slogan is "Big Kids Helping Little Kids" because we donate a portion of our profits to children's charities.
We are looking for a clean, modern, "cool" design that represents the points given above. The site should be fun but easy on the eyes. Navigation should intuitive and easy to find. I would say we are looking for a design that would look and feel at home with Quenby products websites. it should look like a comic book / super hero business website and not a technology product website.
Target Market(s)
Our target demographic is 15 to 35 year old males.
Industry/Entity Type
Business
Coding
Coded - Design and coding required
Number of Pages Required
2 page
Font styles to use
Other font styles liked:
- Comicpro or font similar to our logo
Requirements
Must have
- Tradoo "button" or image that takes them directly to our Tradoo items for sale page here... http://www.tradoo.example/sch/vantelpanels/m.html?_nkw=&_armrs=1&_from=&_ipg=25&_trksid=p3692
- A widget that cycles through our items listed for sale. Prefer something that slides through the items, perhaps showing 4 to 6 items at a time. Tradoo user ID is vantelpanels
- Our slogan - “Big Kids Helping Little Kids”.
- Our mission statement - "To support children’s charities with a portion of our profits. We believe happy kids become happy adults."
- Contact info - email = martin@vantelpanels.example, phone number 555-210-3389, mail = PO Box 482 Elizabethtown Pa 17099
Nice to have
- separate page for charities supported with links to their information page. We currently support the Young Ones Hope Circle in Hershey (http://www.larkfieldyohc.example/index.cfm?fuseaction=cms.home) and the Larkfield Valley Children's Hospital(http://www.larkfieldvalley.example/web/childrens)
- clicking on email in contacts should open a window to generate email message
Should not have
- too childish or cartoony
- too bright or too busy
- blatant use or copies of trademarked characters (like Skyvaultor, Nightwren, ect)

```html
<!DOCTYPE html>
<html lang="en">
<head>
<meta charset="utf-8">
<title>Vantel Panels &amp; Collectibles</title>
<link href="https://fonts.googleapis.com/css2?family=Roboto:wght@400;500;700&family=Lobster&family=Open+Sans:wght@400;600;700&display=swap" rel="stylesheet">
<style>
:root{
  --red:#d0101b;
  --red-dark:#b20d17;
  --navy:#1b2a6b;
  --ink:#333333;
  --muted:#555555;
  --teal:#3d89a8;
  --paper:#ecd9a8;
  --paper-light:#f3e6c4;
  --line:#e2e2e2;
  --white:#ffffff;
  --page-top:#e9e8e4;
}
*{box-sizing:border-box;margin:0;padding:0}
html,body{width:886px;height:1200px;overflow:hidden}
body{position:relative;background:var(--white);font-family:'Roboto',sans-serif;color:var(--ink)}
.abs{position:absolute}

.top-band{left:0;top:0;width:886px;height:520px;background:linear-gradient(180deg,#eeede9 0%,#e4e4df 60%,#ecebe7 100%)}

.call{left:73px;top:32px;display:flex;align-items:center;gap:9px}
.call-icon{width:34px;height:34px;border:1.5px solid #555;border-radius:50%;display:flex;align-items:center;justify-content:center}
.call-title{font-size:14.5px;color:var(--red);font-weight:400;line-height:1.2}
.call-number{font-size:11.5px;color:var(--ink);margin-top:5px;letter-spacing:.3px}

.shop-link{left:690px;top:28px;width:122px;height:44px;display:flex;align-items:center;justify-content:flex-end;font-family:'Roboto',sans-serif;font-weight:700;font-size:32px;color:var(--navy);text-decoration:none;letter-spacing:-1px}

.nav{left:73px;top:93px;width:740px;height:41px;background:var(--red);border-radius:3px 3px 0 0}
.nav a{position:absolute;top:0;line-height:41px;font-size:11px;color:var(--white);text-decoration:none;letter-spacing:.2px}

.brand{left:385px;top:30px;width:116px;height:144px}
.brand-name{position:absolute;left:0;top:50px;width:116px;text-align:center;font-family:'Roboto',sans-serif;font-weight:700;font-size:17px;line-height:1.05;color:var(--red)}
.brand-tag{position:absolute;left:0;top:92px;width:116px;text-align:center;font-family:'Roboto',sans-serif;font-weight:700;font-size:7.5px;color:var(--ink);letter-spacing:.3px}

.hero{left:73px;top:134px;width:740px;height:340px;background:radial-gradient(ellipse at 65% 45%,var(--paper-light) 0%,var(--paper) 70%,#e2cc95 100%);box-shadow:0 14px 14px -10px rgba(0,0,0,.35)}
.hero-photo{position:absolute;left:0;top:0;width:270px;height:340px;background:linear-gradient(180deg,#e6d6ad 0%,#d9c8a0 40%,#b8514a 75%,#c63a30 100%);opacity:.85}
.slogan{position:absolute;left:361px;top:88px;font-family:'Lobster',cursive;font-size:41px;line-height:56px;color:var(--teal)}
.dots{position:absolute;left:368px;top:226px;display:flex;align-items:center;gap:6px}
.dot{width:7px;height:7px;border-radius:50%;background:#333}
.dot.active{width:13px;height:13px;border:1.5px solid var(--red);background:radial-gradient(circle,var(--red) 0 3.5px,transparent 4px)}

.section-title{font-size:18px;font-weight:400;color:var(--ink)}
.carousel-arrows{left:774px;top:549px;display:flex;gap:2px}
.carousel-arrows span{width:18px;height:18px;background:#eeeeee;border:1px solid #e0e0e0;display:flex;align-items:center;justify-content:center}

.card{top:585px;width:174px;height:225px;background:linear-gradient(180deg,#fff 60%,#f3f3f3 100%);border:1px solid var(--line);box-shadow:0 1px 2px rgba(0,0,0,.06)}
.card-art{width:100%;height:163px}
.card-title{position:absolute;left:10px;top:177px;font-family:'Open Sans',sans-serif;font-size:10px;color:var(--ink)}
.card-price{position:absolute;left:10px;top:197px;font-size:12px;color:var(--red);font-weight:500}

.block-title{top:855px;font-size:14.5px;font-weight:400;color:var(--ink);letter-spacing:.3px}
.block-img{top:879px;width:225px;height:131px}
.block-text{top:1025px;width:230px;font-family:'Open Sans',sans-serif;font-size:8.3px;line-height:15px;color:var(--muted)}
.btn{top:1066px;height:24px;background:var(--navy);color:var(--white);font-family:'Open Sans',sans-serif;font-weight:700;font-size:8px;display:flex;align-items:center;justify-content:center;border-radius:2px;text-decoration:none}

.details-title{left:583px;top:856px;font-size:13px;color:var(--ink);letter-spacing:.3px}
.form-panel{left:584px;top:878px;width:228px;height:212px;border:1px solid var(--line);background:var(--white)}
.notch{left:724px;top:861px}
.field{left:603px;width:192px;height:32px;border:1px solid #d6d6d6;border-radius:2px;font-family:'Open Sans',sans-serif;font-size:9px;color:var(--ink);padding-left:12px;display:flex;align-items:center;background:var(--white)}
.field.focus{border:1.5px solid #4a7bd0}
.send{left:603px;top:1033px;width:192px;height:34px;background:var(--navy);color:var(--white);font-family:'Roboto',sans-serif;font-size:15px;display:flex;align-items:center;justify-content:center;border-radius:2px}

.footer{left:0;top:1121px;width:886px;height:79px;background:var(--red)}
.copyright{position:absolute;left:72px;top:20px;font-family:'Open Sans',sans-serif;font-size:8.5px;color:var(--white)}
.footer-links{position:absolute;left:72px;top:45px;font-family:'Open Sans',sans-serif;font-size:7.5px;color:var(--white)}
.footer-links a{color:var(--white);text-decoration:none}
.social{position:absolute;top:29px;width:20px;height:20px;border:1px solid rgba(255,255,255,.75);border-radius:50%}
</style>
</head>
<body>

<div class="abs top-band"></div>

<div class="abs call">
  <div class="call-icon">
    <svg width="16" height="16" viewBox="0 0 24 24"><path d="M6.6 10.8c1.4 2.8 3.8 5.1 6.6 6.6l2.2-2.2c.3-.3.7-.4 1-.2 1.1.4 2.3.6 3.6.6.6 0 1 .4 1 1V20c0 .6-.4 1-1 1C10.6 21 3 13.4 3 4c0-.6.4-1 1-1h3.5c.6 0 1 .4 1 1 0 1.3.2 2.5.6 3.6.1.3 0 .7-.2 1z" fill="#333"/></svg>
  </div>
  <div>
    <div class="call-title">Call Us Now!</div>
    <div class="call-number">+555-210-3389</div>
  </div>
</div>

<a class="abs shop-link" href="http://www.tradoo.example/sch/vantelpanels/m.html?_nkw=&amp;_armrs=1&amp;_from=&amp;_ipg=25&amp;_trksid=p3692">Tradoo</a>

<nav class="abs nav">
  <a href="#" style="left:22px">HOME</a>
  <a href="#" style="left:98px">ABOUT US</a>
  <a href="#" style="left:194px">COMIC BOOKS</a>
  <a href="#" style="left:455px">MY ACCOUNT</a>
  <a href="#" style="left:569px">REVIEWS</a>
  <a href="#" style="left:658px">CONTACT US</a>
</nav>

<div class="abs hero">
  <div class="hero-photo" role="img" aria-label="Photo of a child in a red cape and mask standing on a red stool, fist raised"></div>
  <div class="slogan">Big Kids Helping<br>Little Kids</div>
  <div class="dots"><span class="dot active"></span><span class="dot"></span><span class="dot"></span><span class="dot"></span></div>
</div>

<div class="abs brand">
  <svg width="116" height="144" viewBox="0 0 116 144" style="position:absolute;left:0;top:0;filter:drop-shadow(0 2px 3px rgba(0,0,0,.25))">
    <path d="M58 2 L114 18 L114 112 L58 142 L2 112 L2 18 Z" fill="#fff" stroke="#e6e6e6"/>
  </svg>
  <div class="brand-name">VANTEL<br>PANELS</div>
  <div class="brand-tag">&amp; COLLECTIBLES</div>
</div>

<h2 class="abs section-title" style="left:73px;top:546px">Comic Books</h2>
<div class="abs carousel-arrows">
  <span><svg width="6" height="8" viewBox="0 0 6 8"><path d="M5 1 L2 4 L5 7" stroke="#333" fill="none"/></svg></span>
  <span><svg width="6" height="8" viewBox="0 0 6 8"><path d="M1 1 L4 4 L1 7" stroke="#333" fill="none"/></svg></span>
</div>

<div class="abs card" style="left:73px">
  <div class="card-art" role="img" aria-label="Illustration of two cartoon kid heroes in masks before a city skyline" style="background:linear-gradient(180deg,#4c5688 0%,#5a5f8e 60%,#3d3f66 100%)"></div>
  <div class="card-title">LOREM IPSUM DOLOR SETAM</div>
  <div class="card-price">$105.55</div>
</div>
<div class="abs card" style="left:262px">
  <div class="card-art" role="img" aria-label="Illustration of a caped child reading on a brick chimney above a town" style="background:linear-gradient(180deg,#9fb3c9 0%,#c9d3dc 55%,#9e5e45 100%)"></div>
  <div class="card-title">LOREM IPSUM DOLOR SETAM</div>
  <div class="card-price">$105.55</div>
</div>
<div class="abs card" style="left:450px">
  <div class="card-art" role="img" aria-label="Illustration of a blue-suited flying heroine over a night city" style="background:linear-gradient(180deg,#3d8fb5 0%,#2e6f98 60%,#1f4d6e 100%)"></div>
  <div class="card-title">LOREM IPSUM DOLOR SETAM</div>
  <div class="card-price">$105.55</div>
</div>
<div class="abs card" style="left:639px">
  <div class="card-art" role="img" aria-label="Painted illustration of a boy in a red mask and cape" style="background:linear-gradient(180deg,#4f7f86 0%,#8fa7a3 50%,#c9b89e 100%)"></div>
  <div class="card-title">LOREM IPSUM DOLOR SETAM</div>
  <div class="card-price">$105.55</div>
</div>

<h3 class="abs block-title" style="left:73px">OUR MISSION</h3>
<div class="abs block-img" style="left:73px;background:linear-gradient(180deg,#9fd4d0 0%,#7fc3c0 60%,#5a8f86 100%)" role="img" aria-label="Photo of a girl in a green mask and red cape raising her fist"></div>
<p class="abs block-text" style="left:73px">To support children’s charities with a portion of our profits. We believe happy kids become happy adults</p>
<a class="abs btn" href="#" style="left:73px;width:65px">READ MORE</a>

<h3 class="abs block-title" style="left:327px">OUR DONATION</h3>
<div class="abs block-img" style="left:327px;background:linear-gradient(180deg,#8fb2d6 0%,#6f8fb4 50%,#c79a7e 100%)" role="img" aria-label="Photo of hands holding a boxed superhero building toy set"></div>
<p class="abs block-text" style="left:327px">Lorem ipsum dolor sit amet, consectetur adipisu cing elit. Sed eleifend quam sit amet nunc luctus eu vultate l</p>
<a class="abs btn" href="#" style="left:327px;width:82px">DONATION NOW</a>

<h3 class="abs details-title">DETAILS ABOUT YOU</h3>
<div class="abs form-panel"></div>
<svg class="abs notch" width="42" height="18" viewBox="0 0 42 18"><path d="M0 17.5 L21 1 L42 17.5" fill="#fff" stroke="#e2e2e2"/><rect x="1" y="17" width="40" height="2" fill="#fff"/></svg>
<div class="abs field focus" style="top:901px">Your Name</div>
<div class="abs field" style="top:945px">E _mail</div>
<div class="abs field" style="top:987px">Phone</div>
<div class="abs send">SEND</div>

<footer class="abs footer">
  <div class="copyright">©2015 VANTELPANELS , ALL RIGHTS RESERVED.</div>
  <div class="footer-links">
    <a href="#">HOME</a> &nbsp;|&nbsp; <a href="#">ABOUT VANTELPANELS</a> &nbsp;|&nbsp; <a href="#">COMIC BOOKS</a> &nbsp;|&nbsp; <a href="#">GALLERY</a> &nbsp;|&nbsp; <a href="#">PRICING</a> &nbsp;|&nbsp; <a href="#">CONTACT US</a>
  </div>
  <span class="social" style="left:741px"></span>
  <span class="social" style="left:766px"></span>
  <span class="social" style="left:792px"></span>
</footer>

</body>
</html>
```